Business Card Design

www.bellwaterridge.com.au

Bellwater Ridge Bed and Breakfast
A unique property with spectacular views situated in a peaceful quiet court surrounded by other quality homes. Set back from the street, this wonderful residence has plenty of space. The huge paved driveway has tonnes of off street parking

Relax in the beautifully landscaped lawn area with mature trees. The stunning balcony & deck is an ideal place to sit & watch the spectacular sunsets through the tree tops. Just wonderful!

The self-contained Bed and Breakfast has its own separate entrance door and consists of a large lounge/ kitchenette with sink & a separate bedroom. The bathroom has a glass shower screen, toilet & vanity unit.
If you are looking for your own piece of paradise in an ideal established setting with plenty of room then you must stay at Bellwater ridge
This really is a slice of Heaven so come & stay!

- Established landscaped gardens & lawn areas
- paved driveway - loads of off street parking
- Splendid balcony with glorious views
- Close to shopping & transport

We welcome you to relax and unwind in the charm of our modern country feel bed and breakfast in the Northern Suburbs of Adelaide, offering privacy and relaxation, it is perfect for couples
This self-contained bed & breakfast will provide you with a “home away from home”, including breakfast provisions and all the comfort and modern conveniences you’d expect Bellwater Ridge is perfect whether you’re on a holiday visit to Adelaide or here for business.
Enjoy the many activities Adelaide has to offer, we are positioned in the Northern Suburbs for you to easily travel to the Adelaide Hills or Barossa Wine region.
Bellwater Ridge B & B is in a fantastic location for whatever you want to do on your visit to South Australia. Nestled within walking distance to the Cobbler Creek or visit our world renowned wine regions. Of course, we can help and point you in the right direction.

Shopping

14 Bellwater Court
Salisbury Heights SA 5109

Dennis & Maureen Pellham
0412 555 648 or 0413 555 927
www.bellwaterridge.com.au
dennis@bellwaterridge.com.au

```html
<!DOCTYPE html>
<html lang="en">
<head>
<meta charset="utf-8">
<title>Bellwater Ridge Bed and Breakfast</title>
<link href="https://fonts.googleapis.com/css2?family=Roboto:wght@100;300&display=swap" rel="stylesheet">
<style>
  :root {
    --card-bg: #eff1e3;
    --heading-olive: #a3aa7c;
    --body-sage: #6f785f;
  }
  html, body {
    margin: 0;
    padding: 0;
    width: 1200px;
    height: 692px;
    overflow: hidden;
    background: var(--card-bg);
  }
  .card {
    position: relative;
    width: 1200px;
    height: 692px;
    background: var(--card-bg);
    font-family: "Roboto", Arial, sans-serif;
  }
  .headline {
    position: absolute;
    top: 82px;
    left: 0;
    width: 1200px;
    margin: 0;
    text-align: center;
    font-weight: 100;
    font-size: 55px;
    line-height: 61px;
    color: var(--heading-olive);
  }
  .features {
    position: absolute;
    top: 272px;
    left: 128px;
    margin: 0;
    padding: 0;
    list-style: none;
    font-weight: 300;
    font-size: 45px;
    line-height: 83.5px;
    color: var(--body-sage);
    white-space: nowrap;
  }
  .features li::before {
    content: "\00B7\00A0";
  }
  .features .gardens { letter-spacing: 0; }
  .features .parking { letter-spacing: 1.1px; }
  .features .balcony { letter-spacing: 3.6px; }
  .features .transport { letter-spacing: 5.2px; }
</style>
</head>
<body>
  <main class="card">
    <h1 class="headline">Modern Country-Feel Bed and Breakfast<br>in the Northern Suburbs of Adelaide.</h1>
    <ul class="features">
      <li class="gardens">Established landscaped gardens &amp; lawn areas.</li>
      <li class="parking">Paved driveway - loads of off street parking.</li>
      <li class="balcony">Splendid balcony with glorious views.</li>
      <li class="transport">Close to shopping &amp; public transport.</li>
    </ul>
  </main>
</body>
</html>
```